Business Card Design

Art work over image with business name and phone number. We do automotive wire repair. Some sort of auto theme. Thanks!
Updates

I would like to see the images I uploaded in the card.  Thanks!

Target Market(s)

Auto body repair shops

Industry/Entity Type

Automotive

Contact Information for Business Card

VOLTLINE PROS

602-555-0193

Requirements
Nice to have
• Raised lettering?

```html
<!DOCTYPE html>
<html lang="en">
<head>
<meta charset="utf-8">
<title>Voltline Pros – Business Cards</title>
<link href="https://fonts.googleapis.com/css2?family=Michroma&display=swap" rel="stylesheet">
<style>
  :root {
    --bg-light: #e6e6e6;
    --bg-dark: #5a5a5a;
    --card-black: #0d0d0d;
    --signal-yellow: #f2f02a;
    --ink: #141414;
    --interior-blue: #3d4fa8;
    --interior-violet: #5b4f86;
    --interior-deep: #1c2352;
  }
  html, body {
    margin: 0;
    width: 1200px;
    height: 900px;
    overflow: hidden;
  }
  body {
    background: radial-gradient(ellipse at 50% 40%, var(--bg-light) 0%, #b4b4b4 55%, var(--bg-dark) 100%);
    font-family: "Michroma", sans-serif;
    position: relative;
  }
  .card {
    position: absolute;
    left: 320px;
    width: 560px;
    height: 320px;
    overflow: hidden;
    box-shadow: 0 10px 24px rgba(0,0,0,0.35);
  }
  /* Front */
  .card-front {
    top: 80px;
    background: var(--card-black);
  }
  .interior-photo {
    position: absolute;
    left: 0; right: 0;
    top: 24px;
    height: 236px;
    background:
      linear-gradient(180deg, rgba(120,150,230,0.6) 0%, rgba(0,0,0,0) 30%),
      linear-gradient(100deg, var(--interior-deep) 0%, var(--interior-blue) 35%, var(--interior-violet) 60%, #8b8fb8 80%, var(--interior-deep) 100%);
  }
  .front-title {
    position: absolute;
    left: 0; right: 0;
    top: 96px;
    text-align: center;
    margin: 0;
    color: var(--signal-yellow);
    -webkit-text-stroke: 1px var(--ink);
    font-size: 38px;
    letter-spacing: 5px;
    font-weight: 400;
    line-height: 1;
    white-space: nowrap;
  }
  .front-tagline {
    position: absolute;
    left: 0; right: 0;
    top: 150px;
    text-align: center;
    margin: 0;
    color: var(--signal-yellow);
    -webkit-text-stroke: 0.6px var(--ink);
    font-size: 19px;
    letter-spacing: 4px;
    line-height: 1;
    white-space: nowrap;
  }
  /* Back */
  .card-back {
    top: 500px;
    background: #2a2622;
  }
  .connectors-photo {
    position: absolute;
    inset: 0;
    background:
      radial-gradient(ellipse at 20% 30%, #d8d4cc 0%, rgba(216,212,204,0) 30%),
      radial-gradient(ellipse at 70% 25%, #5b5550 0%, rgba(91,85,80,0) 40%),
      linear-gradient(120deg, #3a3430 0%, #5a4a40 40%, #4a4a52 70%, #6a6058 100%);
  }
  .back-graphics {
    position: absolute;
    inset: 0;
  }
  .back-name, .back-phone {
    position: absolute;
    margin: 0;
    color: var(--ink);
    white-space: nowrap;
    line-height: 1;
  }
  .back-name {
    left: 312px;
    top: 187px;
    font-size: 16px;
    letter-spacing: 3px;
  }
  .back-phone {
    left: 252px;
    top: 239px;
    font-size: 22px;
    letter-spacing: 2px;
  }
</style>
</head>
<body>
  <section class="card card-front">
    <div class="interior-photo" role="img" aria-label="Photo of a modern car interior with dashboard and steering wheel in blue light"></div>
    <h1 class="front-title">VOLTLINE PROS</h1>
    <p class="front-tagline">AUTOMOTIVE WIRE REPAIR</p>
  </section>

  <section class="card card-back">
    <div class="connectors-photo" role="img" aria-label="Close-up photo of white and black automotive wiring harness connectors"></div>
    <svg class="back-graphics" width="560" height="320" viewBox="0 0 560 320" aria-hidden="true">
      <polygon points="430,0 560,0 560,320 180,320" fill="rgba(0,0,0,0.35)"/>
      <line x1="432" y1="0" x2="182" y2="320" stroke="var(--signal-yellow)" stroke-width="5"/>
      <polygon points="293,175 560,175 560,215 262,215" fill="var(--signal-yellow)"/>
      <polygon points="254,225 560,225 560,275 215,275" fill="var(--signal-yellow)"/>
    </svg>
    <p class="back-name">VOLTLINE PROS</p>
    <p class="back-phone">602-555-0193</p>
  </section>
</body>
</html>
```